Velmoro Consulting Business

** Please add the content information from my old business card
1. I would like to see a two sided business card with both options with the 1st Option--Sketch Nest-new WHITE BACKGROUND LOGO
2 nd Option-Sketch Nest - new BLACK- Background Logo
3rd -Option a business card with my Photo on the card
Please add the new word to the card information:
EXECUTION
AS THE OWNER'S REP
WE AIM TO ACHIEVE YOUR
INFRASTRUCTURE VISION with
OUR SPECIALIZATION & EXECUTION in:

FUNDING Planning
BUSINESS Planning
INFRASTRUCTURE Planning
PROJECT Management
Since 2012
_____________________________________________________________________
I want to get spot uv raised printing. I was liking a a nice rich white linen paper stock with black writing & NOT A COLORED CARD other than a variety of white or black cards concept

```html
<!DOCTYPE html>
<html lang="en">
<head>
<meta charset="utf-8">
<title>Velmoro Consulting – Business Cards</title>
<link href="https://fonts.googleapis.com/css2?family=Montserrat:wght@400;500;600;700&display=swap" rel="stylesheet">
<style>
  :root {
    --stage: #3a3a3a;
    --ink: #000000;
    --paper: #ffffff;
    --accent: #e8193c;
    --text-grey: #333333;
    --mist: #e4e4e4;
  }
  html, body {
    margin: 0;
    padding: 0;
    width: 1200px;
    height: 1200px;
    overflow: hidden;
    background: var(--stage);
    font-family: "Montserrat", Arial, sans-serif;
  }
  .card {
    position: absolute;
    left: 200px;
    width: 800px;
    background: var(--paper);
    overflow: hidden;
  }
  .card--front { top: 106px; height: 458px; }
  .card--back { top: 636px; height: 456px; }

  .brand-panel {
    position: absolute;
    top: 0; left: 0; bottom: 0;
    background: var(--ink);
  }
  .card--front .brand-panel { width: 330px; }
  .card--back .brand-panel { width: 267px; }

  .brand-name {
    position: absolute;
    transform: translate(-50%, -50%);
    color: var(--paper);
    font-weight: 700;
    letter-spacing: -1px;
    margin: 0;
    white-space: nowrap;
  }
  .card--front .brand-name { left: 165px; top: 246px; font-size: 54px; }
  .card--back .brand-name { left: 133px; top: 176px; font-size: 44px; }

  .skyline-area {
    position: absolute;
    background: linear-gradient(180deg, var(--paper) 0%, var(--mist) 100%);
  }
  .card--front .skyline-area { left: 506px; top: 318px; width: 280px; height: 140px; }
  .card--back .skyline-area { left: 464px; top: 292px; width: 322px; height: 164px; }

  .accent-bar {
    position: absolute;
    left: 320px; top: 83px;
    width: 22px; height: 293px;
    background: var(--accent);
  }

  .pitch {
    position: absolute;
    left: 388px; top: 100px;
    color: var(--ink);
  }
  .pitch__title {
    margin: 0 0 13px;
    font-size: 27px;
    font-weight: 700;
    letter-spacing: 0.5px;
    line-height: 1.1;
  }
  .pitch__intro {
    margin: 0 0 9px;
    font-size: 17.5px;
    font-weight: 500;
    line-height: 20px;
    white-space: nowrap;
  }
  .pitch__intro strong { font-weight: 700; }
  .services {
    list-style: none;
    margin: 0; padding: 0;
    font-size: 22px;
    font-weight: 500;
    line-height: 28px;
  }
  .services li { white-space: nowrap; }
  .tag {
    display: inline-block;
    padding: 0 4px;
    margin-right: 2px;
    line-height: 24px;
    color: var(--paper);
    font-weight: 700;
    letter-spacing: 0.3px;
  }
  .tag--red { background: var(--accent); }
  .tag--black { background: var(--ink); }
  .pitch__since {
    margin: 8px 0 0;
    font-size: 17px;
    font-weight: 700;
  }

  .name-band {
    position: absolute;
    left: 251px; top: 146px;
    width: 549px; height: 42px;
    background: var(--accent);
  }
  .contact {
    position: absolute;
    left: 287px; top: 146px;
  }
  .contact__name {
    margin: 0;
    height: 42px;
    line-height: 42px;
    font-size: 30.5px;
    font-weight: 600;
    color: var(--paper);
    white-space: nowrap;
  }
  .contact__role {
    margin: 7px 0 14px;
    font-size: 16.5px;
    font-weight: 500;
    letter-spacing: 1.6px;
    color: var(--accent);
    white-space: nowrap;
  }
  .contact__lines {
    margin: 0;
    font-size: 22px;
    line-height: 28px;
    color: var(--text-grey);
    white-space: nowrap;
  }
  .contact__label { color: var(--accent); font-weight: 500; }
  .contact__web { color: var(--accent); font-weight: 700; }
  .contact__offices {
    margin: 11px 0 0;
    font-size: 19px;
    color: var(--text-grey);
    white-space: nowrap;
  }
</style>
</head>
<body>

<section class="card card--front">
  <div class="brand-panel">
    <p class="brand-name">Velmoro</p>
  </div>
  <div class="skyline-area" role="img" aria-label="Outline illustration of city buildings"></div>
  <div class="accent-bar"></div>

  <div class="pitch">
    <h2 class="pitch__title">EXECUTION</h2>
    <p class="pitch__intro">
      AS THE <strong>OWNER'S REP</strong><br>
      WE AIM TO ACHIEVE YOUR<br>
      INFRASTRUCTURE VISION with<br>
      OUR SPECIALIZATION &amp; EXECUTION in:
    </p>
    <ul class="services">
      <li><span class="tag tag--red">FUNDING</span>Planning</li>
      <li><span class="tag tag--black">BUSINESS</span>Planning</li>
      <li><span class="tag tag--red">INFRASTRUCTURE</span>Planning</li>
      <li><span class="tag tag--black">PROJECT</span>Management</li>
    </ul>
    <p class="pitch__since">Since 2012</p>
  </div>
</section>

<section class="card card--back">
  <div class="brand-panel">
    <p class="brand-name">Velmoro</p>
  </div>
  <div class="skyline-area" role="img" aria-label="Outline illustration of city buildings"></div>
  <div class="name-band"></div>

  <div class="contact">
    <h1 class="contact__name">Marisol Duquette-Hanan</h1>
    <p class="contact__role">CEO / LEAD PROJECT MANAGER</p>
    <p class="contact__lines">
      <span class="contact__label">C</span> 867.555.0142<br>
      <span class="contact__label">E</span> mari@velmoro.ca<br>
      <span class="contact__web">www.velmoro.ca</span>
    </p>
    <p class="contact__offices">Kestrel Bay NT &nbsp;•&nbsp; Alder Falls NB</p>
  </div>
</section>

</body>
</html>
```